IT Network Consultancy - Business Card

t4 linkways is a IT network consultancy based in London. We're looking for a smart, modern and professional business card design. Our website is here: www.t4linkways.co.uk

Key things that should be included on the card (with examples):

Company Logo
Name
Position / Job Title: Network Consultant
Mobile Phone Number: +44 (0) 7700 900418
Land Line: +44 (0) 1632 960274
Email Address: name@t4linkways.co.uk
Web Site URL: www.t4linkways.co.uk

Target Market(s)

Large enterprise / global companies / corporates

Industry/Entity Type

Business

Requirements
Must have
• Incorporate our logo - which is attached to the project. They are in AI format (can be opened in Inkscape).

The design should be double sided and fit on a UK standard 85mm × 55mm card and be in a format that retains the quality when printed.
Nice to have
• The project does not have to conform to the colour of our website but this should give you inspiration of the style we like.
Should not have
• Bright colours. Pictures are not necessary.

```html
<!DOCTYPE html>
<html lang="en">
<head>
<meta charset="utf-8">
<title>t4 linkways – Business Card</title>
<link rel="stylesheet" href="https://fonts.googleapis.com/css2?family=Quicksand:wght@400;500;600;700&display=swap">
<style>
  :root {
    --page-bg: #dcdcdc;
    --card-dark: #58595a;
    --card-light: #727a7b;
    --stripe: #6e7a82;
    --accent: #8d9aa4;
    --text-light: #f2f3f3;
    --text-soft: #e4e6e7;
    --label: #8e9ba6;
  }
  * { margin: 0; padding: 0; box-sizing: border-box; }
  html, body {
    width: 1200px;
    height: 1200px;
    overflow: hidden;
    background: var(--page-bg);
    font-family: "Quicksand", sans-serif;
  }
  .card {
    position: absolute;
    left: 217px;
    width: 773px;
    height: 500px;
    background: linear-gradient(30deg, var(--card-dark) 0%, var(--card-light) 100%);
    overflow: hidden;
    color: var(--text-light);
  }
  .card--front { top: 56px; }
  .card--back { top: 611px; }
  .card__stripes {
    position: absolute;
    inset: 0;
    width: 100%;
    height: 100%;
  }
  .card__stripes polygon { fill: var(--stripe); }

  .brand {
    position: absolute;
    left: 0;
    right: 0;
    top: 200px;
    text-align: center;
    font-size: 66px;
    font-weight: 500;
    letter-spacing: 3px;
    color: var(--text-light);
  }

  .identity {
    position: absolute;
    left: 292px;
    top: 78px;
    width: 434px;
    text-align: center;
  }
  .identity__name {
    font-size: 64px;
    font-weight: 400;
    font-variant: small-caps;
    letter-spacing: 3px;
    line-height: 1;
    color: var(--text-light);
  }
  .identity__rule {
    height: 6px;
    margin-top: 8px;
    background: var(--accent);
  }
  .identity__role {
    margin-top: 10px;
    font-size: 24px;
    font-weight: 500;
    font-variant: small-caps;
    letter-spacing: 1.5px;
    color: var(--text-soft);
  }

  .contact {
    position: absolute;
    left: 18px;
    top: 289px;
    padding-left: 17px;
    border-left: 11px solid var(--accent);
    min-height: 122px;
    line-height: 19px;
  }
  .contact__label {
    display: block;
    font-size: 15px;
    font-weight: 700;
    color: var(--label);
  }
  .contact__value {
    display: block;
    font-size: 17px;
    font-weight: 400;
    color: var(--text-soft);
  }

  .website {
    position: absolute;
    left: 0;
    right: 0;
    bottom: 16px;
    text-align: center;
    font-size: 23px;
    font-weight: 500;
    letter-spacing: 2px;
    color: var(--text-light);
  }
</style>
</head>
<body>

  <section class="card card--front" aria-label="Business card front">
    <svg class="card__stripes" viewBox="0 0 644 416" preserveAspectRatio="none" aria-hidden="true">
      <polygon points="31,0 104,0 0,203 0,61"/>
      <polygon points="644,208 644,330 604,416 544,416"/>
    </svg>
    <div class="brand">t4 linkways</div>
  </section>

  <section class="card card--back" aria-label="Business card back">
    <svg class="card__stripes" viewBox="0 0 644 416" preserveAspectRatio="none" aria-hidden="true">
      <polygon points="31,0 104,0 0,205 0,62"/>
      <polygon points="644,208 644,330 604,416 544,416"/>
    </svg>

    <div class="identity">
      <h1 class="identity__name">Daniel Hart</h1>
      <div class="identity__rule"></div>
      <p class="identity__role">Network Consultant</p>
    </div>

    <div class="contact">
      <span class="contact__label">phone.</span>
      <span class="contact__value">+44 (0) 1632 960274</span>
      <span class="contact__label">mobile.</span>
      <span class="contact__value">+44 (0) 7700 900418</span>
      <span class="contact__label">email.</span>
      <span class="contact__value">danielhart@t4linkways.co.uk</span>
    </div>

    <div class="website">www.t4linkways.co.uk</div>
  </section>

</body>
</html>
```